RK Tannery Construction Inc.

Design a new business card for our construction company
To be removed from current card:
Delete 25 years
Delete Tenant fit up Renovations section

```html
<!DOCTYPE html>
<html lang="en">
<head>
<meta charset="utf-8">
<title>RK Tannery Construction Inc. – Business Card</title>
<link href="https://fonts.googleapis.com/css2?family=Montserrat:wght@400;500;600;700;800&display=swap" rel="stylesheet">
<style>
  :root {
    --teal: #247a6f;
    --teal-dark: #1f6d63;
    --purple: #5b2a86;
    --ink: #2e2e2e;
    --rule: #9a9a9a;
    --paper: #ffffff;
    --backdrop: #3a3a3a;
  }
  * { box-sizing: border-box; margin: 0; padding: 0; }
  html, body {
    width: 1200px; height: 1200px; overflow: hidden;
    background: var(--backdrop);
    font-family: "Montserrat", Arial, sans-serif;
  }
  .stage {
    width: 1200px; height: 1200px;
    display: flex; flex-direction: column; align-items: center; justify-content: center;
    gap: 50px;
  }
  .card {
    position: relative;
    width: 940px; height: 537px;
    border-radius: 36px;
    overflow: hidden;
  }
  /* Front */
  .card-front { background: var(--paper); }
  .wordmark {
    position: absolute; left: 0; right: 0; top: 95px;
    text-align: center; color: var(--teal);
    font-weight: 800; line-height: 1;
  }
  .wordmark .line-main { display: block; font-size: 64px; letter-spacing: 1px; }
  .wordmark .line-sub { display: block; font-size: 29px; letter-spacing: 9px; margin-top: 8px; }
  .person {
    position: absolute; left: 90px; top: 258px;
    color: var(--ink);
  }
  .person-name {
    color: var(--teal); font-weight: 700; font-size: 30px; letter-spacing: 0.5px;
    margin-bottom: 16px;
  }
  .contact-line {
    display: flex; align-items: center; gap: 12px;
    font-size: 19px; line-height: 1.25; margin-bottom: 9px;
  }
  .contact-line svg { width: 20px; height: 20px; flex: none; fill: var(--teal); }
  .divider {
    position: absolute; left: 478px; top: 245px;
    width: 1px; height: 120px; background: var(--rule);
  }
  .company-info { position: absolute; left: 515px; top: 250px; color: var(--ink); }
  .company-info .contact-line { font-size: 17px; margin-bottom: 7px; align-items: flex-start; }
  .company-info .contact-line svg { margin-top: 1px; }
  .accent-line {
    position: absolute; left: 0; right: 0; top: 398px; height: 7px;
    background: var(--purple);
  }
  .service-band {
    position: absolute; left: 0; right: 0; top: 416px; bottom: 0;
    background: var(--teal);
    display: flex; flex-direction: column; align-items: center; justify-content: center;
    color: #fff; font-weight: 600; letter-spacing: 1px; text-align: center;
  }
  .service-band .services-main { font-size: 20px; margin-bottom: 6px; }
  .service-band .services-sectors { font-size: 17px; }
  /* Back */
  .card-back {
    background: var(--teal);
    display: flex; align-items: center; justify-content: center;
  }
  .card-back .wordmark {
    position: static; color: #fff;
  }
  .card-back .wordmark .line-main { font-size: 92px; }
  .card-back .wordmark .line-sub { font-size: 41px; letter-spacing: 13px; margin-top: 12px; }
</style>
</head>
<body>
<main class="stage">
  <section class="card card-front" aria-label="Card front">
    <div class="wordmark">
      <span class="line-main">RK TANNERY</span>
      <span class="line-sub">CONSTRUCTION INC.</span>
    </div>

    <div class="person">
      <p class="person-name">DANIEL TANNERY</p>
      <p class="contact-line">
        <svg viewBox="0 0 24 24" aria-hidden="true"><path d="M7 1h10a2 2 0 0 1 2 2v18a2 2 0 0 1-2 2H7a2 2 0 0 1-2-2V3a2 2 0 0 1 2-2zm0 3v14h10V4zm5 15.5a1.2 1.2 0 1 0 0 2.4 1.2 1.2 0 0 0 0-2.4z"/></svg>
        555-318-7724
      </p>
      <p class="contact-line">
        <svg viewBox="0 0 24 24" aria-hidden="true"><path d="M2 5h20v14H2zm2 2v.4l8 5.6 8-5.6V7zm0 2.8V17h16V9.8l-8 5.6z"/></svg>
        daniel@rktanneryconst.ca
      </p>
    </div>

    <div class="divider"></div>

    <div class="company-info">
      <p class="contact-line">
        <svg viewBox="0 0 24 24" aria-hidden="true"><path d="M6.6 10.8a15.1 15.1 0 0 0 6.6 6.6l2.2-2.2a1 1 0 0 1 1-.25 11.4 11.4 0 0 0 3.6.57 1 1 0 0 1 1 1V20a1 1 0 0 1-1 1A17 17 0 0 1 3 4a1 1 0 0 1 1-1h3.5a1 1 0 0 1 1 1c0 1.25.2 2.45.57 3.57a1 1 0 0 1-.25 1z"/></svg>
        555-210-4480 ext. 221
      </p>
      <p class="contact-line">
        <svg viewBox="0 0 24 24" aria-hidden="true"><path d="M12 2a10 10 0 1 0 0 20 10 10 0 0 0 0-20zm6.9 6h-2.9a15.6 15.6 0 0 0-1.4-3.6A8 8 0 0 1 18.9 8zM12 4c.8 1.2 1.5 2.5 1.9 4h-3.8c.4-1.5 1.1-2.8 1.9-4zM4.3 14a8.2 8.2 0 0 1 0-4h3.4a16.5 16.5 0 0 0 0 4zm.8 2h2.9c.3 1.3.8 2.5 1.4 3.6A8 8 0 0 1 5.1 16zM8 8H5.1a8 8 0 0 1 4.3-3.6C8.8 5.5 8.3 6.7 8 8zm4 12c-.8-1.2-1.5-2.5-1.9-4h3.8c-.4 1.5-1.1 2.8-1.9 4zm2.3-6H9.7a14.7 14.7 0 0 1 0-4h4.6a14.7 14.7 0 0 1 0 4zm.3 5.6c.6-1.1 1.1-2.3 1.4-3.6h2.9a8 8 0 0 1-4.3 3.6zm1.7-5.6a16.5 16.5 0 0 0 0-4h3.4a8.2 8.2 0 0 1 0 4z"/></svg>
        www.rktanneryconstruction.ca
      </p>
      <p class="contact-line">
        <svg viewBox="0 0 24 24" aria-hidden="true"><path d="M12 2a7 7 0 0 0-7 7c0 5.2 7 13 7 13s7-7.8 7-13a7 7 0 0 0-7-7zm0 9.5A2.5 2.5 0 1 1 12 6.5a2.5 2.5 0 0 1 0 5z"/></svg>
        <span>2175 Millbrook Rd.<br>Suite 100, Kingston, ON K7L 4V1</span>
      </p>
    </div>

    <div class="accent-line"></div>
    <div class="service-band">
      <p class="services-main">TURN KEY OPERATIONS | PROJECT MANAGEMENT</p>
      <p class="services-sectors">OFFICE | RETAIL | INSTITUTIONAL</p>
    </div>
  </section>

  <section class="card card-back" aria-label="Card back">
    <div class="wordmark">
      <span class="line-main">RK TANNERY</span>
      <span class="line-sub">CONSTRUCTION INC.</span>
    </div>
  </section>
</main>
</body>
</html>
```